Stylist/Barber Standup Sign for Hair Regrowth Company

We want to design an attractive and eye-catching sign for hair stylists and barbers to sit on their workstations to attract the attention of their clients regarding hair loss and encourage them to speak to their stylist about it of they are would like to seek treatment.
50% of men and 25% of women suffer from hair loss but most are in denial that it is happening or too embarrassed to talk about it.

Copy for the flyer is as follows:

[Section 1:]
This flyer has been placed here/designed to spark conversation about hair loss

[Section 2:]
The truth is...
73% of people believe their hair is thinning
They are right

[Section 3:]
If you've got questions, your stylist or barber has answers.

Additional Background Information:

Primary target audience is men between the ages of 25-45, secondary target audience is men 46-60

Current Consumer Perception? (in the first person) “I’ve been thinking about my hair. I think it’s getting thinner and I’m scared, worried and don’t know what to do. But I don’t know if there is anything that really works. I’ve tried other things and nothing‘s worked.”

Tonality of materials? Very guy friendly, matter of fact, authoritative, its what you might hear from your best friend. Confident. Encouraging, but with a sense of urgency.

Please use our brand colors, but do not include our logo or brand name.
Colors are as follows:
Green: #4ca26f
Light Grey: #999999
Dark Grey: #262626

I have attached print templates in both PDF and Jpeg, please use those to provide final ready to print documents if you are selected.

Target Market(s)

Industry/Entity Type

Health And Wellness

Font styles to use
Sans Serif

Colors
00a990
ffffff
333333
cbcbcb

Requirements
Must have
• We want to get across the following messaging. Ideally you will submit a design using our copy and if you think you can do better, please feel free to submit another design with your own copy/messaging. If you can do it better we would love to select you :-)
• Our copy?
• This flyer has been placed here/designed to spark conversation about hair loss
• The truth is...
• 73% of people believe their hair is thinning
• They are right
• If you've got questions, your stylist or barber has answers
• Also please use our brand colors:
• Green: #4ca26f
• Light Grey: #999999
• Dark Grey: #262626
Should not have
• dont add any logos, images or ornate design. this needs to be simple, easy to ready and eye catching.
• do not use the color red in any capacity.

```html
<!DOCTYPE html>
<html lang="en">
<head>
<meta charset="utf-8">
<title>Hair Loss Conversation Sign</title>
<link rel="stylesheet" href="https://fonts.googleapis.com/css2?family=Bebas+Neue&display=swap">
<style>
  :root {
    --backdrop: #000000;
    --card: #ffffff;
    --card-edge: #3a3a3a;
    --green: #17ad8f;
    --dark: #333333;
    --light: #cbcbcb;
    --ink-light: #ffffff;
    --ink-dark: #333333;
  }
  html, body {
    margin: 0;
    padding: 0;
    overflow: hidden;
    background: var(--backdrop);
  }
  .canvas {
    position: relative;
    width: 1200px;
    height: 1200px;
    background: var(--backdrop);
    overflow: hidden;
    font-family: "Bebas Neue", "Oswald", sans-serif;
  }
  .sign {
    position: absolute;
    left: 167px;
    top: 25px;
    width: 877px;
    height: 1137px;
    background: var(--card);
    box-shadow: 0 0 0 1px var(--card-edge);
  }
  .panel {
    position: absolute;
    left: 192px;
    width: 827px;
  }
  .panel--intro { top: 53px; height: 319px; background: var(--green); }
  .panel--truth { top: 402px; height: 425px; background: var(--dark); }
  .panel--answer { top: 857px; height: 281px; background: var(--light); }

  .line {
    position: absolute;
    margin: 0;
    line-height: 1;
    white-space: nowrap;
    font-weight: 400;
    letter-spacing: 1px;
  }
  .intro-line { left: 222px; font-size: 64px; color: var(--ink-light); }
  .truth-kicker { left: 228px; top: 442px; font-size: 46px; color: var(--green); }
  .stat-number { left: 228px; top: 487px; font-size: 160px; color: var(--ink-light); letter-spacing: 0; }
  .stat-text { font-size: 66px; color: var(--ink-light); letter-spacing: 2px; }
  .stat-text--first { left: 472px; top: 575px; }
  .stat-text--second { left: 230px; top: 652px; font-size: 74px; letter-spacing: 1px; }
  .verdict { left: 234px; top: 723px; font-size: 86px; color: var(--green); }
  .answer-line { left: 216px; font-size: 66px; color: var(--ink-dark); letter-spacing: 2px; }
</style>
</head>
<body>
<main class="canvas">
  <div class="sign"></div>

  <section class="panel panel--intro"></section>
  <p class="line intro-line" style="top:80px;">This flyer has been placed here /</p>
  <p class="line intro-line" style="top:178px;">designed to spark conversation</p>
  <p class="line intro-line" style="top:276px;">about hair loss</p>

  <section class="panel panel--truth"></section>
  <p class="line truth-kicker">The truth is...</p>
  <p class="line stat-number">73%</p>
  <p class="line stat-text stat-text--first">of people&nbsp; believe</p>
  <p class="line stat-text stat-text--second">that their hair is thinning</p>
  <p class="line verdict">They are right</p>

  <section class="panel panel--answer"></section>
  <p class="line answer-line" style="top:926px;">If you've got questions, your</p>
  <p class="line answer-line" style="top:983px;">stylist or barber has answers</p>
</main>
</body>
</html>
```